Business cards for a high-end menswear store

I would like to come up with a design for our business cards.
Two different ones: one for general sales and one for the owner. It is a high-end menswear store.

Our address is: 4817 Morneau Boulevard, Montreal, QC, K7P4M2
phone number: 514-286-5937
insta: MAISONVERLAINE
Website: www.maisonverlaine.example
email (general card): info@maisonverlaine.example
email (owner): bastien@maisonverlaine.example

I have attached our logo in an ai and eps file format. You can see our old cards as well. I am looking for a modern and clean look.

Target Market(s)

High-End Clothing Market

Industry/Entity Type

Retail, Clothing, Luxury Clothing

Contact Information for Business Card

Address, Name, Email, Website, Social Info,

Font styles to use
Serif

Colors

Designer to choose colors to be used in the design.

Requirements
Must have
• Address, Name, Email, Website, Social Info,
Nice to have
• QR Code that brings you to the website

```html
<!DOCTYPE html>
<html lang="en">
<head>
<meta charset="utf-8">
<title>Maison Verlaine – Business Cards</title>
<link rel="stylesheet" href="https://fonts.googleapis.com/css2?family=Open+Sans:wght@700&display=swap">
<style>
  :root {
    --tan: #a39370;
    --ink: #221f1f;
    --paper: #ffffff;
    --backdrop: #6d6e72;
  }
  * { margin: 0; padding: 0; box-sizing: border-box; }
  html, body { width: 1200px; height: 1200px; overflow: hidden; }
  body {
    background: var(--backdrop);
    font-family: "Open Sans", Arial, sans-serif;
    font-weight: 700;
    position: relative;
  }
  .card { position: absolute; overflow: hidden; border-radius: 36px; }

  /* Front */
  .card-front { left: 210px; top: 100px; width: 732px; height: 418px; background: var(--tan); }
  .front-tab { position: absolute; top: 125px; width: 31px; height: 165px; background: var(--ink); }
  .front-tab--left { left: 0; border-radius: 0 30px 30px 0; }
  .front-tab--right { right: 0; border-radius: 30px 0 0 30px; }
  .front-rule { position: absolute; top: 209px; left: 31px; right: 31px; height: 5px; background: var(--ink); }
  .brand-name {
    position: absolute; text-align: center; color: var(--ink);
    letter-spacing: 0.4em; white-space: nowrap;
  }
  .card-front .brand-name { left: 0; width: 732px; top: 101px; font-size: 13px; padding-left: 0.4em; }
  .brand-square { position: absolute; background: var(--ink); }
  .card-front .brand-square { left: 266px; top: 123px; width: 186px; height: 187px; }
  .front-web {
    position: absolute; left: 0; width: 732px; top: 382px; text-align: center;
    color: var(--paper); font-size: 15px; letter-spacing: 0.12em;
  }

  /* Back */
  .card-back { left: 207px; top: 632px; width: 735px; height: 415px; background: var(--paper); }
  .back-dark { position: absolute; left: 368px; top: 0; right: 0; bottom: 0; background: var(--ink); }
  .back-band { position: absolute; left: 0; right: 0; top: 403px; height: 12px; background: var(--tan); }
  .back-tab { position: absolute; top: 33px; height: 45px; background: var(--tan); }
  .back-tab--left { left: 0; width: 124px; border-radius: 0 0 45px 0; }
  .back-tab--right { left: 587px; right: 0; border-radius: 45px 0 0 0; }
  .back-notch { position: absolute; left: 368px; top: 107px; width: 44px; height: 252px; background: var(--paper); border-radius: 0 44px 44px 0; }
  .back-title { position: absolute; top: 34px; font-size: 30px; letter-spacing: 0.2em; line-height: 40px; white-space: nowrap; }
  .back-title--light { right: 376px; color: var(--tan); }
  .back-title--dark { left: 378px; color: var(--paper); }
  .card-back .brand-name { left: 76px; width: 198px; top: 142px; font-size: 11px; padding-left: 0.4em; }
  .card-back .brand-square { left: 76px; top: 161px; width: 198px; height: 198px; }

  .contact-icon { position: absolute; left: 368px; width: 30px; height: 30px; }
  .contact-line {
    position: absolute; left: 425px; color: var(--tan);
    font-size: 11px; line-height: 17px; white-space: nowrap;
  }
</style>
</head>
<body>

<section class="card card-front" aria-label="Card front">
  <div class="front-tab front-tab--left"></div>
  <div class="front-tab front-tab--right"></div>
  <div class="front-rule"></div>
  <div class="brand-name">MAISON VERLAINE</div>
  <div class="brand-square"></div>
  <div class="front-web">WWW.MAISONVERLAINE.EXAMPLE</div>
</section>

<section class="card card-back" aria-label="Card back">
  <div class="back-dark"></div>
  <div class="back-band"></div>
  <div class="back-tab back-tab--left"></div>
  <div class="back-tab back-tab--right"></div>
  <div class="back-notch"></div>
  <div class="back-title back-title--light">MAISON</div>
  <div class="back-title back-title--dark">VERLAINE</div>

  <div class="brand-name">MAISON VERLAINE</div>
  <div class="brand-square"></div>

  <!-- address -->
  <svg class="contact-icon" style="top:149px" viewBox="0 0 30 30">
    <circle cx="15" cy="15" r="14" fill="#fff" stroke="var(--tan)" stroke-width="1.4"/>
    <path d="M8 15 L15 9 L22 15 Z" fill="var(--tan)"/>
    <rect x="10" y="15" width="10" height="7" fill="var(--tan)"/>
    <rect x="14" y="18" width="2.4" height="4" fill="#fff"/>
  </svg>
  <div class="contact-line" style="top:147px">4817 MORNEAU BOULEVARD<br>Montreal, QC, K7P4M2</div>

  <!-- phone -->
  <svg class="contact-icon" style="top:186px" viewBox="0 0 30 30">
    <circle cx="15" cy="15" r="14" fill="#fff" stroke="var(--tan)" stroke-width="1.4"/>
    <path d="M10 8.5 l2.5 -0.5 l1.8 3.6 l-1.6 1.4 c0.8 1.8 2.2 3.2 4 4 l1.4 -1.6 l3.6 1.8 l-0.5 2.5 c-6 0.6 -11.8 -5.2 -11.2 -11.2 z" fill="var(--tan)"/>
  </svg>
  <div class="contact-line" style="top:193px">514-286-5937</div>

  <!-- social -->
  <svg class="contact-icon" style="top:223px" viewBox="0 0 30 30">
    <circle cx="15" cy="15" r="14" fill="#fff" stroke="var(--tan)" stroke-width="1.4"/>
  </svg>
  <div class="contact-line" style="top:230px">MAISONVERLAINE</div>

  <!-- email -->
  <svg class="contact-icon" style="top:260px" viewBox="0 0 30 30">
    <circle cx="15" cy="15" r="14" fill="#fff" stroke="var(--tan)" stroke-width="1.4"/>
    <path d="M8 13 L15 8 L22 13 V21 H8 Z" fill="var(--tan)"/>
    <path d="M8 13 L15 18 L22 13" fill="none" stroke="#fff" stroke-width="1"/>
  </svg>
  <div class="contact-line" style="top:267px">INFO@MAISONVERLAINE.EXAMPLE</div>

  <!-- web -->
  <svg class="contact-icon" style="top:298px" viewBox="0 0 30 30">
    <circle cx="15" cy="15" r="14" fill="#fff" stroke="var(--tan)" stroke-width="1.4"/>
    <circle cx="15" cy="15" r="7.5" fill="var(--tan)"/>
    <g fill="none" stroke="#fff" stroke-width="0.8">
      <ellipse cx="15" cy="15" rx="3.2" ry="7.5"/>
      <line x1="15" y1="7.5" x2="15" y2="22.5"/>
      <line x1="7.5" y1="15" x2="22.5" y2="15"/>
      <line x1="8.5" y1="11.5" x2="21.5" y2="11.5"/>
      <line x1="8.5" y1="18.5" x2="21.5" y2="18.5"/>
    </g>
  </svg>
  <div class="contact-line" style="top:305px">WWW.MAISONVERLAINE.EXAMPLE</div>
</section>

</body>
</html>
```